Business school needs a web design

Who We are:
KRVT is a small business school that offers programs in Project Management. The school is based in West Africa and welcomes students from the whole area. Our aim is to become one of the reference business schools in Africa.

Project Brief:
The site will include all informations relevant for different types of visitors that we have: actual and future students, companies, mass media, future employees, ect. It will present information about subscription, list of programs, presentation of the school and its team,etc.

What We want:
This competition is for Design only no coding! We need design for two pages.
We did some wireframing for the home page and the list of programs page. We made them just to show how we imagine the website would look like. But we encourage creative designs, so you don't have to stick to the wireframe models.

Sites We like:
http://www.ravenmoorcollege.example/
http://www.belvantis.example/fr/etudes.html
http://www.qtl.example/mba/Pages/default.aspx

Color schemes
The logo of the school is red and black. So the color scheme of the website should match that. For the rest, it is opened to your imagination.
Updates

The payment for the project is now garanteed. Good luck to you all !

Target Market(s)

The target market is diversified because we have students of different ages, also company representatives or employees that might visit the website for recruitment purposes. But the majority of our audience should be aged between 20 - 30 years.

Industry/Entity Type

Small Business

Requirements
Must have
• The design must include two pages: a home page and another interior page : might be the list of programs or any other page relevant to the domain. The Home page must include a slide show at the beginning.
The background page must be white.
Nice to have
• The use of flat design for this project is preferred.
The use of Pelican scaffold as a base for the design is an asset.

```html
<!DOCTYPE html>
<html lang="fr">
<head>
<meta charset="utf-8">
<title>KRVT – Programmes et Formations</title>
<link href="https://fonts.googleapis.com/css2?family=Open+Sans:wght@300;400;600;700&family=Oswald:wght@500;600&display=swap" rel="stylesheet">
<style>
:root{
  --red:#c4141b;
  --red-dark:#a50f15;
  --ink:#333333;
  --muted:#555555;
  --link:#2a6fb0;
  --page:#ffffff;
  --band:#f1f1f1;
  --line:#dedede;
  --header:#f8f8f8;
}
*{box-sizing:border-box;margin:0;padding:0}
html,body{width:1148px;height:1200px;overflow:hidden}
body{position:relative;background:var(--page);font-family:"Open Sans",Arial,sans-serif;color:var(--ink)}
.abs{position:absolute}

/* header */
.site-header{position:absolute;left:0;top:0;width:1148px;height:76px;background:var(--header);border-top:3px solid #222}
.brand{position:absolute;left:240px;top:14px;display:flex;align-items:center;gap:8px}
.brand-mark{width:16px;height:16px;background:var(--red)}
.brand-name{font-family:"Open Sans",sans-serif;font-weight:700;font-size:24px;color:var(--red);letter-spacing:1px}
.utility-links{position:absolute;right:423px;top:20px;font-size:7.6px;color:var(--muted);white-space:nowrap}
.utility-links a{color:var(--muted);text-decoration:none}
.utility-links a.active{color:var(--red)}
.utility-links .sep{margin:0 4px;color:#aaa}
.search{position:absolute;left:739px;top:17px;width:158px;height:18px;border:1px solid #ccc;background:#fff;font-size:9px;color:#777;padding:3px 7px}
.search svg{position:absolute;right:5px;top:3px}
.main-nav{position:absolute;left:409px;top:43px;width:488px;height:24px;background:var(--red);display:flex;border-radius:2px}
.main-nav a{flex:auto;color:#fff;font-size:9.5px;font-weight:700;text-decoration:none;text-align:center;line-height:24px;border-right:1px solid var(--red-dark)}
.main-nav a:last-child{border-right:0}

/* hero */
.hero{position:absolute;left:0;top:76px;width:1148px;height:248px;background:linear-gradient(90deg,#3e4b4f 0%,#5a6a6e 35%,#8b9698 60%,#c9ced0 85%,#e6e9ea 100%)}
.hero-copy{position:absolute;left:241px;top:50px;color:#fff}
.hero-kicker{font-size:18px;font-weight:700}
.hero-title{font-size:33px;font-weight:300;margin-top:4px;line-height:1.1}
.hero-text{font-size:10px;line-height:15px;margin-top:12px;width:250px;color:#e5e5e5}
.hero-btn{display:inline-block;margin-top:20px;width:102px;height:27px;border:1px solid #fff;font-size:10px;font-weight:700;text-align:center;line-height:25px;color:#fff}

/* breadcrumb */
.crumbs-band{position:absolute;left:0;top:324px;width:1148px;height:31px;background:var(--band);border-bottom:1px solid var(--line)}
.crumbs{position:absolute;left:240px;top:9px;font-size:9px;font-weight:600;color:var(--ink)}
.crumbs a{color:var(--red);text-decoration:none}

/* content panel */
.content{position:absolute;left:224px;top:355px;width:691px;height:614px;background:#fff;border-left:1px solid var(--line);border-right:1px solid var(--line);box-shadow:0 0 6px rgba(0,0,0,.06)}
.page-title{position:absolute;left:0;width:1148px;text-align:center;font-family:"Oswald",sans-serif;font-weight:600;font-size:20px;color:var(--red);letter-spacing:.3px}
.title-rule{position:absolute;left:440px;top:411px;width:267px;height:1px;background:var(--line)}
.intro{position:absolute;left:280px;top:421px;width:588px;text-align:center;font-size:10.3px;line-height:14.5px;color:var(--muted)}

.video-box{position:absolute;left:239px;top:497px;width:660px;height:254px;border:1px solid var(--line);background:#fff}
.video-main{position:absolute;left:12px;top:9px;width:426px;height:233px}
.video-frame{position:absolute;left:0;top:0;width:426px;height:214px;background:linear-gradient(135deg,#b7bfc2 0%,#8a7a6c 45%,#5a4a40 75%,#3a3a3a 100%)}
.play{position:absolute;left:186px;top:91px}
.video-bar{position:absolute;left:0;top:214px;width:426px;height:19px;background:#1b1b1b}
.video-progress{position:absolute;left:0;top:0;width:426px;height:3px;background:#555}
.video-progress span{display:block;width:132px;height:3px;background:var(--red)}
.video-time{position:absolute;left:52px;top:5px;font-size:7px;color:#bbb}

.playlist{position:absolute;left:455px;top:9px;width:188px;height:238px;border:1px solid var(--line)}
.thumb{position:absolute;left:17px;width:140px;height:53px;background:linear-gradient(135deg,#c9c2b8,#6d5a4e 60%,#2f2f2f)}
.thumb .tbar{position:absolute;left:0;bottom:0;width:140px;height:6px;background:#1b1b1b;border-top:2px solid var(--red)}
.thumb-cap{position:absolute;left:17px;font-size:9px;color:var(--link)}
.scroll{position:absolute;left:176px;top:6px;width:6px;height:220px;border:1px solid #ccc;border-radius:3px}
.scroll span{position:absolute;left:0;top:38px;width:4px;height:26px;background:#bbb;border-radius:2px}

.section-rule{position:absolute;left:239px;top:784px;width:660px;height:1px;background:var(--line)}
.section-title{position:absolute;left:240px;top:800px;font-family:"Oswald",sans-serif;font-weight:500;font-size:16px;color:var(--red)}
.program{position:absolute;top:835px;width:151px}
.program-img{width:151px;height:88px;border:1px solid var(--line);padding:4px;background:#fff}
.program-img div{width:100%;height:100%}
.program-name{margin-top:10px;font-size:11.5px;font-weight:700;color:#444;padding-left:3px}

/* partners */
.partners{position:absolute;left:0;top:969px;width:1148px;height:51px;background:#ebebeb;border-top:1px solid var(--line);border-bottom:1px solid var(--line)}
.arrow-btn{position:absolute;top:17px}
.partner{position:absolute;top:13px;height:24px;border-radius:3px}

/* footer */
.footer-col{position:absolute;top:1037px;font-size:9px;line-height:15px;color:var(--muted)}
.footer-col h3{font-size:12px;font-weight:600;color:var(--ink);margin-bottom:11px}
.social{display:flex;gap:3px}
.social span{width:19px;height:19px;display:block}
.contact-line{display:flex;align-items:center;gap:8px;margin-top:3px}
.newsletter-input{margin-top:8px;width:142px;height:17px;border:1px solid #bbb;font-size:8px;color:#777;padding:2px 5px}
.subscribe{margin-top:7px;width:59px;height:15px;background:var(--red);color:#fff;font-size:8.5px;font-weight:700;text-align:center;line-height:15px;border-radius:2px}
.footer-rule{position:absolute;left:240px;top:1171px;width:657px;height:1px;background:var(--line)}
.copyright{position:absolute;left:240px;top:1177px;font-size:8px;color:var(--ink)}
</style>
</head>
<body>

<header class="site-header">
  <div class="brand"><span class="brand-mark"></span><span class="brand-name">KRVT</span></div>
  <nav class="utility-links">
    <a class="active" href="#">Repertoire du personnel</a><span class="sep">|</span><a href="#">Blogue</a><span class="sep">|</span><a href="#">Salle de presse</a><span class="sep">|</span><a href="#">Nous joindre</a><span class="sep">|</span><a href="#">Francais</a>
  </nav>
  <div class="search">Search
    <svg width="11" height="11" viewBox="0 0 11 11"><circle cx="4.5" cy="4.5" r="3.5" fill="none" stroke="#777" stroke-width="1.3"/><line x1="7" y1="7" x2="10.5" y2="10.5" stroke="#777" stroke-width="1.5"/></svg>
  </div>
  <nav class="main-nav">
    <a href="#">A propos de l'KRVT</a><a href="#">Programmes et Formations</a><a href="#">Etudiants</a><a href="#">Nouvelles et Evenements</a><a href="#">Entreprises</a>
  </nav>
</header>

<section class="hero" role="img" aria-label="Photo: homme en costume travaillant sur un ordinateur dans un bureau vitré avec vue sur la ville">
  <div class="hero-copy">
    <div class="hero-kicker">An innovative graduate</div>
    <div class="hero-title">School of theology</div>
    <p class="hero-text">Lorem Ipsum is simply dummy text of the printing and type-setting industry. Lorem Ipsum has been</p>
    <span class="hero-btn">MORE INFO</span>
  </div>
</section>

<div class="crumbs-band"><div class="crumbs"><a href="#">Accueil</a> &gt; Programmes et Formations</div></div>

<main class="content"></main>
<h1 class="page-title" style="top:380px">PROGRAMMES ET FORMATIONS</h1>
<div class="title-rule"></div>
<p class="intro">lorem ipsum dolor sit amet, consectetur odipisicing elit, sed do eiusmod tempor incididunt ut lobore et dolore magna aliqua Ut enim ad minim veniam, quis nostrud exercitation ullamco laboris nisi ut aliquip ex ea commodo consequat. Duis aute irure dolor in reprehenderit in voluptate velit esse cillum dolore eu fugiat nulla pariatur. Excepteur sint occaecat cupidatat non proident, sunt in culpa qui officio deserunt mollit anim id est laborum.</p>

<div class="video-box">
  <div class="video-main">
    <div class="video-frame" role="img" aria-label="Vidéo: étudiants réunis autour d'un ordinateur en salle de classe"></div>
    <svg class="play" width="54" height="54" viewBox="0 0 54 54"><circle cx="27" cy="27" r="27" fill="rgba(30,30,30,.7)"/><path d="M21 16 L38 27 L21 38Z" fill="#fff"/></svg>
    <div class="video-bar">
      <div class="video-progress"><span></span></div>
      <svg class="abs" style="left:12px;top:6px" width="30" height="9" viewBox="0 0 30 9"><path d="M0 0 L7 4.5 L0 9Z" fill="#ddd"/><path d="M20 3h3l3-3v9l-3-3h-3z" fill="#ddd"/></svg>
      <span class="video-time">1:18 / 3:16</span>
    </div>
  </div>
  <div class="playlist">
    <div class="thumb" style="top:11px" role="img" aria-label="Miniature vidéo: étudiants en cours"><div class="tbar"></div></div>
    <div class="thumb-cap" style="top:68px">proident, sunt in culpa qui officio</div>
    <div class="thumb" style="top:85px" role="img" aria-label="Miniature vidéo: groupe d'étudiants sur le campus"><div class="tbar"></div></div>
    <div class="thumb-cap" style="top:142px">proident, sunt in culpa qui officio</div>
    <div class="thumb" style="top:159px" role="img" aria-label="Miniature vidéo: étudiants travaillant ensemble"><div class="tbar"></div></div>
    <div class="thumb-cap" style="top:216px">proident, sunt in culpa qui officio</div>
    <div class="scroll"><span></span></div>
  </div>
</div>

<div class="section-rule"></div>
<h2 class="section-title">PROGRAMMES OFFERTS</h2>

<div class="program" style="left:240px"><div class="program-img"><div role="img" aria-label="Photo: étudiante écrivant à son bureau" style="background:linear-gradient(135deg,#8a6f5e,#5b5f7a 60%,#2c2c34)"></div></div><div class="program-name">Placement Testing</div></div>
<div class="program" style="left:409px"><div class="program-img"><div role="img" aria-label="Photo: enseignante devant un tableau" style="background:linear-gradient(135deg,#9aa79a,#c7b9a3 55%,#e2d8c8)"></div></div><div class="program-name">Teacher Education</div></div>
<div class="program" style="left:577px"><div class="program-img"><div role="img" aria-label="Photo: groupe d'étudiants devant des drapeaux" style="background:linear-gradient(135deg,#b9c3cc,#a55a4e 50%,#4d6a3c)"></div></div><div class="program-name">Study Abroad</div></div>
<div class="program" style="left:747px"><div class="program-img"><div role="img" aria-label="Photo: étudiante écrivant à son bureau" style="background:linear-gradient(135deg,#8a6f5e,#5b5f7a 60%,#2c2c34)"></div></div><div class="program-name">Placement Testing</div></div>

<section class="partners" aria-label="Partenaires">
  <svg class="arrow-btn" style="left:240px" width="17" height="17" viewBox="0 0 17 17"><circle cx="8.5" cy="8.5" r="8.5" fill="#aaa"/><path d="M10 4.5 L6 8.5 L10 12.5" fill="none" stroke="#fff" stroke-width="2"/></svg>
  <span class="partner" style="left:278px;width:58px;background:#e08a2e"></span>
  <span class="partner" style="left:397px;width:40px;background:#b79a3a"></span>
  <span class="partner" style="left:463px;width:50px;background:#2f83c6"></span>
  <span class="partner" style="left:537px;width:72px;background:#9db8cc"></span>
  <span class="partner" style="left:634px;width:44px;background:#7a7a7a"></span>
  <span class="partner" style="left:700px;width:60px;background:#d24a3c"></span>
  <span class="partner" style="left:781px;width:72px;background:#9db8cc"></span>
  <svg class="arrow-btn" style="left:881px" width="17" height="17" viewBox="0 0 17 17"><circle cx="8.5" cy="8.5" r="8.5" fill="#aaa"/><path d="M7 4.5 L11 8.5 L7 12.5" fill="none" stroke="#fff" stroke-width="2"/></svg>
</section>

<footer>
  <div class="footer-col" style="left:240px">
    <h3>Suivez-nous</h3>
    <div class="social" aria-label="Réseaux sociaux">
      <span style="background:#3b5998"></span><span style="background:#2aa9e0"></span><span style="background:#d32f2f"></span><span style="background:#1e78b4"></span>
    </div>
  </div>
  <div class="footer-col" style="left:373px">
    <h3>A propos</h3>
    A propos de KRVT<br>Admissions Calendrier de<br>l'école Offres d'emploi<br>Repertoire du personnel
  </div>
  <div class="footer-col" style="left:505px">
    <h3>Etudiants</h3>
    Accueil étudiants Profils<br>des étudiants<br>Entreprises<br>Blogue<br>Anciens<br>Formations
  </div>
  <div class="footer-col" style="left:620px">
    <h3>KRVT</h3>
    12, Rue des Baobabs<br>Quartier Nord, près du<br>Jardin des Lumières
    <div class="contact-line" style="margin-top:10px"><svg width="8" height="10" viewBox="0 0 8 10"><path d="M2 0 L4 2.5 L2.8 3.8 Q3.5 6 5.2 7.2 L6.5 6 L8 8.5 L6.5 10 Q1 8 0 1.5Z" fill="#444"/></svg>(221) 30 412 77 18</div>
    <div class="contact-line"><svg width="8" height="10" viewBox="0 0 8 10"><path d="M2 0 L4 2.5 L2.8 3.8 Q3.5 6 5.2 7.2 L6.5 6 L8 8.5 L6.5 10 Q1 8 0 1.5Z" fill="#444"/></svg>(221) 70 539 24 06</div>
  </div>
  <div class="footer-col" style="left:755px">
    <h3 style="display:flex;align-items:center;gap:10px">Infolettre <svg width="17" height="11" viewBox="0 0 17 11"><rect x=".5" y=".5" width="16" height="10" fill="none" stroke="#888"/><path d="M.5 .5 L8.5 6.5 L16.5 .5" fill="none" stroke="#888"/></svg></h3>
    <div style="width:150px">Créée pour former des profession-nels de haut niveau capables de planifier et de réaliser des projets</div>
    <div class="newsletter-input">Enter Your Email...</div>
    <div class="subscribe">Subscribe</div>
  </div>
  <div class="footer-rule"></div>
  <div class="copyright">@KRVT, 2013 Tous droits reserves</div>
</footer>

</body>
</html>
```